Geschäftspapiere für Gastronomie Nutzeis
Zielgruppe
Frostalm GmbH 'Velvet Chill & Co.' ist eine Firma die sich auf Herstellung und Vertrieb von Nutzeis für hochkarätige Gastronomie, Hotellerie, Catering und Eventagenturen spezialisiert hat.
Hergestellt und vertrieben werden neben dem traditionellen Eiswürfel und Crushed-Ice aus einer Eismaschine, handgeschnittene, kristallklare, individuelle Eiswürfel in verschiedenen Größen und Formen.
Aufgabenstellung
Gerne auch mit Wasserzeichen indem das Q aus dem Logo verwendet werden kann. Slogan lautet Velvet Chill & Co.. Ziel ist es hochwertig, luxuriös, seriös auf den Leser des Briefpapiers zu wirken. Alle relevante Daten wie HRB Nummer, Umsatzsteuer ID, Kontakt, Bankverbindung etc. sollen Platz bekommen und es soll Druckfertige Datei sein. Die Datei wäre als Word Dokument für uns vom Vorteil um die Daten ggf. zu ändern in der Zukunft. Das Briefpapier dient für Briefe, Rechungen, Angebote, Verträge etc.
Hier wären die Daten die auf das Briefpapier kommen sollen.
Die PNG Logo Datei wurde durch Vektor PDF Datei ersetzt.

```html
<!DOCTYPE html>
<html lang="de">
<head>
<meta charset="utf-8">
<title>Frostalm GmbH – Briefpapier</title>
<link rel="stylesheet" href="https://fonts.googleapis.com/css2?family=Arimo:wght@400&family=Open+Sans:wght@400;600&display=swap">
<style>
  :root {
    --accent: #d67b67;
    --ink: #2b2b2b;
    --backdrop: #ececec;
    --paper: #ffffff;
    --fold: #999999;
    --signature-fill: #f4f4f4;
  }
  * { box-sizing: border-box; margin: 0; padding: 0; }
  html, body { width: 1200px; height: 1010px; overflow: hidden; background: var(--backdrop); }
  .letterhead {
    position: absolute; left: 261px; top: 24px;
    width: 678px; height: 962px;
    background: var(--paper);
    box-shadow: 0 2px 10px rgba(0,0,0,.12);
    font-family: "Arimo", Arial, sans-serif;
    color: var(--ink);
    overflow: hidden;
  }
  .top-rule { position: absolute; left: 0; top: 0; width: 100%; height: 4px; background: var(--accent); }
  .company-name {
    position: absolute; right: 58px; top: 48px;
    font-family: "Arimo", Arial, sans-serif; font-weight: 400;
    font-size: 26px; letter-spacing: 0; color: var(--accent);
  }
  .contact {
    position: absolute; left: 452px; top: 96px;
    padding-left: 14px; border-left: 1px solid var(--ink);
    font-family: "Open Sans", Arial, sans-serif; font-style: normal;
    font-size: 9px; line-height: 13px;
  }
  .contact .company { font-weight: 600; }
  .contact-line { display: flex; align-items: center; gap: 6px; }
  .contact-line svg { width: 8px; height: 8px; fill: var(--accent); flex: none; }
  .contact .spaced { margin-top: 3px; }
  .return-address {
    position: absolute; left: 80px; top: 176px;
    font-family: "Open Sans", Arial, sans-serif; font-size: 6.5px;
    padding-bottom: 2px; border-bottom: 1px solid var(--ink);
  }
  .fold-mark { position: absolute; left: 0; width: 16px; height: 1px; background: var(--fold); }
  .fold-mark.upper { top: 321px; }
  .fold-mark.lower { top: 641px; }
  .letter-body { position: absolute; left: 80px; top: 292px; width: 520px; font-size: 12.4px; line-height: 15.2px; }
  .salutation { margin-bottom: 8px; }
  .letter-body p { margin-bottom: 15px; }
  .signature { width: 110px; height: 42px; margin-top: 4px; background: var(--signature-fill); }
  .footer-band {
    position: absolute; left: 0; top: 866px; width: 100%; height: 62px;
    background: var(--accent); color: #fff;
    display: flex; align-items: center; padding: 0 36px;
    font-family: "Open Sans", Arial, sans-serif; font-size: 7.6px; line-height: 11px;
  }
  .footer-col { padding: 0 16px; border-left: 1px solid rgba(255,255,255,.8); }
  .footer-col:first-child { border-left: none; padding-left: 0; }
</style>
</head>
<body>
<main class="letterhead">
  <div class="top-rule"></div>

  <div class="company-name">Frostalm</div>

  <address class="contact">
    <div class="company">Frostalm GmbH</div>
    <div>Kühlhausweg 9</div>
    <div>85399 Lindenried</div>
    <div class="contact-line spaced"><svg viewBox="0 0 10 10"><path d="M2 0h2l1 3-1.5 1a6 6 0 0 0 2.5 2.5L7 5l3 1v2a2 2 0 0 1-2 2A8 8 0 0 1 0 2a2 2 0 0 1 2-2z"/></svg>+49 (0)8000 / 12 34 567</div>
    <div class="contact-line"><svg viewBox="0 0 10 10"><path d="M0 2h10v6H0z"/></svg>info@frostalm-eis.de</div>
    <div class="contact-line"><svg viewBox="0 0 10 10"><circle cx="5" cy="5" r="5"/></svg>www.frostalm-eis.de</div>
  </address>

  <div class="return-address">Frostalm GmbH | Kühlhausweg 9 | 85399 Lindenried</div>
  <span class="fold-mark upper"></span>
  <span class="fold-mark lower"></span>

  <section class="letter-body">
    <div class="salutation">Herr Lindner</div>
    <p>Lorem ipsum dolor sit amet, consectetur adipiscing elit. Proin tincidunt, lectus id malesuada cursus, lorem augue egestas magna, ut mattis orci ante ut arcu. Sed mauris tellus, fermentum quis ligula nec, posuere pulvinar eros. Nam at mi quis velit pellentesque finibus. Donec lacus velit, faucibus mollis dolor nec, finibus pellentesque orci. Duis sed dictum elit, ut posuere arcu. Phasellus ac dolor et ante consequat rutrum nec nec tortor. Donec consequat, nibh sit amet pulvinar faucibus, turpis magna venenatis diam, vel pretium eros erat vestibulum nulla.</p>
    <p>Sed pretium ac enim eu viverra. Aliquam ac est eget magna convallis convallis. Aenean augue purus, finibus eget turpis quis, finibus dignissim nibh. Phasellus viverra lobortis dignissim. Duis varius turpis in sapien accumsan facilisis. Sed vehicula gravida diam a interdum. Nullam convallis ligula id erat egestas consequat. Integer consectetur ex vel aliquet iaculis. Vestibulum molestie sodales mauris, at tincidunt risus pellentesqu.</p>
    <p>Mauris facilisis, lectus at accumsan tincidunt, dui magna imperdiet sem, quis tempor est lectus eu ipsum. Praesent in fermentum nisl. Maecenas at lorem at odio interdum iaculis. Pellentesque cursus nulla nunc, ut suscipit nulla maximus et. Donec maximus rhoncus metus, vel laoreet nisi pretium sit amet. Donec posuere enim lectus, vitae aliquam augue tincidunt dignissim. Morbi vitae congue velit, quis elementum.</p>
    <div class="signature" role="img" aria-label="Handschriftliche Unterschrift von Jonas Weber"></div>
  </section>

  <footer class="footer-band">
    <div class="footer-col">Bankverbindung:<br>Bank: Nordtal Bank eG</div>
    <div class="footer-col">IBAN: DE00 1234 5678 9000 1122 33<br>BIC: NTBKDEF1XXX</div>
    <div class="footer-col">Handelsregister: HRB 100 200<br>Registergericht: Amtsgericht Lindenried<br>Umsatzsteuer ID: DE000111222</div>
    <div class="footer-col">Vertreten durch die Geschäftsführer:<br>Lena Hartwig, Paul Steinbach</div>
  </footer>
</main>
</body>
</html>
```